Label design

Description
I want you to design a label for a skin care product line. I’ve provide the picture of the jar we are using along with the logo. Please note that the logo is available in different colors as well. (See attached) I would like the label to be very clean and straight to the point. Here is some info that I would like to see on the label:
240G
Net wt 8.0z

The content of the jar can be refer to as:

Body cream
Crème de corps
Body butter
Fade cream
Skin tone cream
Lotion pour le corps
Clarifying Body cream
Lightening Cream

The content is also made an exotic component that: “Extraits de noisette de palmiers” meaning nuts extract.

The brand NAME is: Miravé
The tag line is: Be yourself, love yourself

Industry/Entity Type

Skin Care Product

```html
<!DOCTYPE html>
<html lang="en">
<head>
<meta charset="utf-8">
<title>Miravé Clarifying Body Cream Label</title>
<link rel="stylesheet" href="https://fonts.googleapis.com/css2?family=Josefin+Sans:wght@300;400&display=swap">
<style>
  :root {
    --page-bg: #f3f3f3;
    --label-white: #ffffff;
    --label-shade: #e4e5e7;
    --brand-orange: #ee7a2b;
    --text-orange: #e8702a;
    --gold-deep: #cf8a36;
    --gold-mid: #e3a54c;
    --gold-light: #f6e39a;
  }
  * { margin: 0; padding: 0; box-sizing: border-box; }
  html, body {
    width: 1200px;
    height: 1200px;
    overflow: hidden;
    background: var(--page-bg);
  }
  .canvas {
    width: 1200px;
    height: 1200px;
    display: flex;
    align-items: center;
    justify-content: center;
  }
  .label {
    position: relative;
    width: 1020px;
    height: 760px;
    background: linear-gradient(90deg, var(--label-shade) 0%, var(--label-white) 18%, var(--label-white) 70%, var(--label-shade) 100%);
    font-family: "Josefin Sans", "Century Gothic", sans-serif;
    color: var(--text-orange);
    text-align: center;
  }
  .gold-band {
    position: absolute;
    left: 0;
    width: 100%;
    height: 18px;
    background: linear-gradient(90deg, var(--gold-deep) 0%, var(--gold-mid) 35%, var(--gold-light) 62%, var(--gold-mid) 82%, var(--gold-deep) 100%);
  }
  .gold-band--top { top: 0; }
  .gold-band--bottom { bottom: 0; }
  .brand-name {
    position: absolute;
    top: 190px;
    left: 0;
    width: 100%;
    font-size: 128px;
    font-weight: 300;
    line-height: 1;
    color: var(--brand-orange);
    letter-spacing: 1px;
  }
  .tagline {
    position: absolute;
    top: 340px;
    left: 0;
    width: 100%;
    font-size: 28px;
    font-weight: 400;
  }
  .product-name {
    position: absolute;
    top: 440px;
    left: 0;
    width: 100%;
    font-size: 52px;
    font-weight: 300;
  }
  .ingredient {
    position: absolute;
    top: 512px;
    left: 0;
    width: 100%;
    font-size: 27px;
    font-weight: 300;
  }
  .net-weight {
    position: absolute;
    bottom: 70px;
    font-size: 30px;
    font-weight: 300;
  }
  .net-weight--imperial { left: 30px; }
  .net-weight--metric { right: 40px; }
</style>
</head>
<body>
  <main class="canvas">
    <section class="label">
      <div class="gold-band gold-band--top"></div>
      <h1 class="brand-name">Miravé</h1>
      <p class="tagline">Be yourself, love yourself</p>
      <h2 class="product-name">Clarifying Body cream</h2>
      <p class="ingredient">Extraits de noisette de palmiers</p>
      <p class="net-weight net-weight--imperial">Net wt 8.0z</p>
      <p class="net-weight net-weight--metric">240g</p>
      <div class="gold-band gold-band--bottom"></div>
    </section>
  </main>
</body>
</html>
```